Poster for a Bicycle show/Expo

We need a poster for a Bicycle show/Expo and sustainable transport. Exhibitors will sell bikes, cycling clothing, accessories, etc. ...
This show is annual and the Poster is for the 2016 edition.

Your concept must be compatible in a landscape format. (We will ourselves adaptations of different formats.)
Width: 210 mm
Height: 297 mm
It's necessary for us to have the source file (vector) for make, later, the different format (flyers, website, ...)

Content of the Poster:
- 1 big picture (one of the two attached)
- Big title (typo-title worked): « Foire du Rouet » (« Salon » or « Salon du » can be small and « Vélo » big.)
- Subtitle: « et de la mobilité durable »
- Date: « 18, 19 et 20 mars 2016 » or « 18-20 mars 2016 »
- Place: « Halle RTP - Gare de Plantaz »
- Text line 1: « www.foire-du-rouet.ch »
- Text line 2: « Entrée gratuite »
- Text line 3: « Ve 18 mars de 17h à 20h - Sa 19 mars de 10h à 18h - Di 20 mars de 10h à 17h »
- Please, leave a zone in the poster for sponsors logos
(The predominant information (most visible) are: « Vélo » and « 18, 19 et 20 mars 2016 » or « 18-20 mars 2016 »)

Target Market(s)

Bicycle fan

Industry/Entity Type

Sporting Good

Font styles to use
Serif
Sans Serif

Colors
add136
ffffff
ec1f27

Requirements
Must have
• The style must be modern, dynamic, bright colors.

```html
<!DOCTYPE html>
<html lang="fr">
<head>
<meta charset="utf-8">
<title>Foire du Rouet 2016</title>
<link href="https://fonts.googleapis.com/css2?family=Titillium+Web:wght@300;400;600;700;900&display=swap" rel="stylesheet">
<style>
  :root {
    --green: #add136;
    --white: #ffffff;
    --red: #ec1f27;
    --navy: #1a3f78;
    --sky-top: #1b56a0;
    --sky-mid: #4c97d6;
    --sky-low: #a9d5f2;
    --grass: #6fae2c;
    --grass-dark: #3f7f1c;
    --schedule: #2f74c0;
    --rider-dark: #2b3440;
    --rider-mid: #6d7077;
    --rider-warm: #b5553f;
  }
  * { margin: 0; padding: 0; box-sizing: border-box; }
  html, body { width: 874px; height: 1200px; overflow: hidden; background: #ffffff; }
  .poster {
    position: relative;
    width: 874px;
    height: 1200px;
    overflow: hidden;
    font-family: "Titillium Web", "Arial Narrow", sans-serif;
    color: var(--white);
  }
  .hero-photo {
    position: absolute;
    inset: 0;
    background:
      linear-gradient(180deg, transparent 0 75%, var(--grass) 80%, var(--grass-dark) 100%),
      linear-gradient(180deg, var(--sky-top) 0%, var(--sky-mid) 40%, var(--sky-low) 75%);
  }
  .hero-rider {
    position: absolute;
    left: 500px; top: 590px;
    width: 370px; height: 420px;
    border-radius: 46% 40% 22% 22%;
    background:
      radial-gradient(ellipse at 55% 30%, var(--rider-warm) 0%, transparent 38%),
      radial-gradient(ellipse at 50% 75%, var(--rider-dark) 0%, var(--rider-mid) 45%, transparent 72%);
    opacity: 0.55;
  }
  .site-url {
    position: absolute;
    left: 34px; top: 34px;
    font-size: 26px; font-weight: 700;
    letter-spacing: 0.5px;
  }
  .entry-tag {
    position: absolute;
    right: 20px; top: 26px;
    width: 320px; height: 60px;
    background: var(--green);
    display: flex; align-items: center; justify-content: center;
    font-size: 31px; font-weight: 700; text-transform: uppercase;
    letter-spacing: 0.5px;
  }
  .title { position: absolute; left: 36px; top: 140px; color: var(--green); line-height: 0.85; }
  .title-small {
    display: block;
    font-size: 96px; font-weight: 300; text-transform: uppercase;
    letter-spacing: 1px;
  }
  .title-big {
    position: absolute;
    left: 228px; top: 78px;
    font-size: 196px; font-weight: 700; text-transform: uppercase;
    letter-spacing: -4px; white-space: nowrap;
  }
  .subtitle {
    position: absolute; left: 290px; top: 425px;
    display: flex; align-items: baseline; gap: 14px;
    text-transform: uppercase; white-space: nowrap;
  }
  .subtitle-lead { font-size: 26px; font-weight: 600; }
  .subtitle-main { font-size: 48px; font-weight: 900; letter-spacing: 0.5px; }
  .date-box {
    position: absolute; left: 20px; top: 588px;
    width: 312px; padding: 10px 18px 12px;
    background: var(--red);
    font-size: 50px; font-weight: 700; line-height: 1;
    text-transform: uppercase;
  }
  .venue {
    position: absolute; left: 34px; top: 738px;
    color: var(--navy);
    font-size: 32px; font-weight: 700; line-height: 1.05;
    text-transform: uppercase;
  }
  .schedule {
    position: absolute; left: 52px; top: 930px;
    list-style: none;
    color: var(--schedule);
    font-size: 22px; font-weight: 700; line-height: 1.35;
    text-transform: uppercase;
  }
</style>
</head>
<body>
<main class="poster">
  <div class="hero-photo" role="img" aria-label="Photo : grand ciel bleu au-dessus d'une colline herbeuse"></div>
  <div class="hero-rider" role="img" aria-label="Photo : une cycliste avec un sac à dos rouge roule sur son vélo dans l'herbe"></div>

  <p class="site-url">www.foire-du-rouet.ch</p>
  <p class="entry-tag">Entrée gratuite</p>

  <h1 class="title">
    <span class="title-small">Foire<br>du</span>
    <span class="title-big">Rouet</span>
  </h1>

  <p class="subtitle">
    <span class="subtitle-lead">et de la</span>
    <span class="subtitle-main">Mobilité durable</span>
  </p>

  <p class="date-box">18, 19 et 20<br>mars 2016</p>

  <p class="venue">Halle RTP<br>Gare de Plantaz</p>

  <ul class="schedule">
    <li>Vendredi 18 mars de 17h à 20h</li>
    <li>Samedi 19 mars de 10h à 18h</li>
    <li>Dimanche 20 mars de 10h à 17h</li>
  </ul>
</main>
</body>
</html>
```